Innovative Consulting Firm Needs New Business Cards and Stationary

Our Innovative Consulting Firm, Larkfield Consulting, is in need of new business cards and stationary designs. We want two-sided cards that incorporate our logo, which is attached. We are looking for something not too formal, but is professional and slick.

Card should have the following information:
Name (ex. Tom Bradley)
Title (ex. Manager)
Address (ex. 24680 Cedar Lane)
Address 2 (ex. Suite 100)
City
State
Zip Code
Mobile
Email

The card should also have our website: www.larkfieldconsulting.example

Industry/Entity Type

Management Consulting

Contact Information for Business Card

Name (ex. Tom Bradley)
Title (ex. Manager)
Address 2 (ex. Suite 100)
City
State
Zip Code
Mobile
Email

Font styles to use
Sans Serif

Requirements
Must have
• The colors on the card must match the colors in the logo. The exact color codes are attached in a pdf.
Nice to have
• The Company's Tagline is "Focused on your Future". This might be nice to incorporate, but not necessary.

```html
<!DOCTYPE html>
<html lang="en">
<head>
<meta charset="utf-8">
<title>Larkfield Consulting – Business Cards</title>
<link rel="stylesheet" href="https://fonts.googleapis.com/css2?family=Barlow:wght@500;600&family=Jost:wght@400;500&display=swap">
<style>
  :root {
    --stage: #97989a;
    --navy: #1f4e79;
    --gold: #f4b41f;
    --white: #ffffff;
    --slate: #4a4a4a;
  }
  * { margin: 0; padding: 0; box-sizing: border-box; }
  html, body { width: 1200px; height: 1200px; overflow: hidden; }
  body { background: var(--stage); position: relative; font-family: "Jost", sans-serif; }

  .card { position: absolute; top: 250px; width: 400px; height: 700px; overflow: hidden; background: var(--white); }
  .card--front { left: 161px; }
  .card--back { left: 653px; background: var(--navy); }
  .card__shapes { position: absolute; inset: 0; }

  .wordmark { position: absolute; left: 0; width: 400px; text-align: center; font-family: "Jost", sans-serif; font-weight: 500; line-height: 1; }
  .wordmark__name { display: block; font-size: 46px; letter-spacing: 1px; }
  .wordmark__sub { display: block; font-size: 11px; letter-spacing: 4px; margin-top: 6px; padding-left: 130px; }
  .card--front .wordmark { top: 150px; color: var(--navy); }
  .card--back .wordmark { top: 240px; color: var(--white); }

  .tagline { position: absolute; left: 0; width: 400px; text-align: center; font-family: "Barlow", sans-serif; font-weight: 500; font-size: 21px; letter-spacing: 0.3px; }
  .card--front .tagline { top: 222px; color: var(--navy); }
  .card--back .tagline { top: 589px; color: var(--slate); font-size: 22px; }

  .person { position: absolute; top: 390px; left: 0; width: 400px; text-align: center; color: var(--white); }
  .person__name { font-size: 31px; font-weight: 500; line-height: 1; letter-spacing: 0.5px; }
  .person__title { font-size: 20px; font-weight: 500; margin-top: 6px; line-height: 1; }

  .contacts { position: absolute; top: 484px; left: 85px; list-style: none; color: var(--white); font-size: 15px; line-height: 1.3; }
  .contacts__item { display: flex; align-items: center; height: 30px; margin-bottom: 22px; }
  .contacts__item--address { height: 40px; margin-bottom: 18px; }
  .contacts__icon { width: 28px; height: 28px; background: var(--white); flex: none; display: flex; align-items: center; justify-content: center; margin-right: 25px; }
  .contacts__icon svg { width: 18px; height: 18px; }
</style>
</head>
<body>
  <section class="card card--front" aria-label="Business card front">
    <svg class="card__shapes" viewBox="0 0 400 700" aria-hidden="true">
      <polygon points="59,0 339,0 199,44" fill="var(--gold)"/>
      <polygon points="0,325 65,325 199,368 334,325 400,325 400,700 0,700" fill="var(--navy)"/>
    </svg>
    <div class="wordmark">
      <span class="wordmark__name">Larkfield</span>
      <span class="wordmark__sub">CONSULTING</span>
    </div>
    <p class="tagline">FOCUSED ON YOUR FUTURE</p>
    <div class="person">
      <p class="person__name">Tom Bradley</p>
      <p class="person__title">Manager</p>
    </div>
    <ul class="contacts">
      <li class="contacts__item contacts__item--address">
        <span class="contacts__icon"><svg viewBox="0 0 24 24"><path d="M12 2a7 7 0 0 0-7 7c0 5 7 13 7 13s7-8 7-13a7 7 0 0 0-7-7zm0 9.5A2.5 2.5 0 1 1 12 6.5a2.5 2.5 0 0 1 0 5z" fill="var(--gold)"/></svg></span>
        <span>24680 Cedar Lane,<br>Springfield QLD 4300</span>
      </li>
      <li class="contacts__item">
        <span class="contacts__icon"><svg viewBox="0 0 24 24"><rect x="2" y="5" width="20" height="14" fill="var(--gold)"/><path d="M2 5l10 8 10-8" fill="none" stroke="var(--white)" stroke-width="1.6"/></svg></span>
        <span>tom@larkfieldconsulting.example</span>
      </li>
      <li class="contacts__item">
        <span class="contacts__icon"><svg viewBox="0 0 24 24"><g fill="none" stroke="var(--gold)" stroke-width="2"><circle cx="12" cy="12" r="9"/><ellipse cx="12" cy="12" rx="4" ry="9"/><path d="M3 12h18M5 7h14M5 17h14"/></g></svg></span>
        <span>www.larkfieldconsulting.example</span>
      </li>
    </ul>
  </section>

  <section class="card card--back" aria-label="Business card back">
    <svg class="card__shapes" viewBox="0 0 400 700" aria-hidden="true">
      <polygon points="64,0 340,0 200,44" fill="var(--white)"/>
      <polygon points="0,475 64,475 200,518 340,475 400,475 400,700 0,700" fill="var(--white)"/>
    </svg>
    <div class="wordmark">
      <span class="wordmark__name">Larkfield</span>
      <span class="wordmark__sub">CONSULTING</span>
    </div>
    <p class="tagline">FOCUSED ON YOUR FUTURE</p>
  </section>
</body>
</html>
```